Need 8.5" x 11" as well as large 11"x17" Posters for our upcoming event

Please include LOGOs in poster
Main logo is Harborview Teen Circle of PL

All high school age faith groups are invited to come and join with 150 to 175 other high school students from various faith traditions to participate in the Harborview Teen Circle of Pine Lakes‘s Annual Kindred Voices Gathering. More than ever, our county and world need young leaders who are willing to learn from each other and build stronger communities!

KINDRED GATHERING
The purpose of this Interfaith Youth Forum is to bring together young people from diverse ethnic, cultural, and religious backgrounds, and to engage them in dialogue. True dialogue is a conversation on a common subject between two or more persons of differing points of view and/or backgrounds. We feel that this commitment to dialogue will affect relationships in a constructive way in our places of worship and in our community.
The forum itself involves having eight religiously diverse high school-age students, one adult, and youth leader around each table to discuss common questions. Our youth leaders act as facilitators, but it is stressed that it is the students we want to hear from.
RSVP for our KINDRED GATHERING before February 18th, 2018
FORUM QUESTIONS Available online at http://htcpl-example.org/home/kindred-fair/

Target Market(s)

Houses of worship, community leaders, High School Students

Industry/Entity Type

Non-Profit

Font styles to use
Serif

Colors
cfdeed
0255a3
f78f20
f37122
f68d4d
faa54b
ffcf3e
ffc214
34a6d7

Requirements
Must have
• Harborview Teen Circle of Pine Lakes's 14th Annual Kindred Gathering & Fair
• TEENS EXPRESSING THEIR FAITH THROUGH ART, MUSIC, AND DIALOGUE
• THIS YEAR'S THEME: “Who Are You?”
• Sunday, March 11th, 2018 11:00am-5:00pm
• Congregation Ner Adamah
• 4187 W Larkmont Rd. Santa Ana, CA 92705
• Email: htcplorg@mailbox-example.com
• Website: HTCPL-example.org
• Facebook: Harborview Teen Circle of Pine Lakes
Nice to have
• Descriptions provided in word doc
Should not have
• -

```html
<!DOCTYPE html>
<html lang="en">
<head>
<meta charset="utf-8">
<title>Kindred Gathering &amp; Fair Poster</title>
<link rel="stylesheet" href="https://fonts.googleapis.com/css2?family=Oswald:wght@500&family=Roboto+Slab:wght@700&family=Libre+Baskerville:ital,wght@0,700;1,700&family=Lato:wght@700&family=PT+Sans:wght@400;700&display=swap">
<style>
  :root {
    --canvas: #e8e6e2;
    --orange: #f37122;
    --orange-soft: #f78f20;
    --navy: #0255a3;
    --sky: #34a6d7;
    --pale: #cfdeed;
    --ink: #3d3f42;
    --body-text: #4a4c4f;
    --band: #d4d9dd;
    --footer-gray: #58595b;
    --footer-blue: #2f86e0;
    --ring: #3b86d4;
  }
  * { box-sizing: border-box; margin: 0; padding: 0; }
  html, body { width: 1200px; height: 1200px; overflow: hidden; background: var(--canvas); }
  .poster {
    position: absolute; left: 151px; top: 20px;
    width: 897px; height: 1160px; overflow: hidden;
    background: linear-gradient(180deg, #d6ebf8 0%, #c4e1f4 55%, #d9edf9 100%);
    box-shadow: 0 4px 18px rgba(0,0,0,.25);
  }
  .poster > * { position: absolute; }
  .hero-photo {
    left: 0; top: 0; width: 897px; height: 360px;
    background: linear-gradient(180deg, #6d1218 0%, #8a2128 22%, #5f7fa6 45%, #9bb6cf 65%, #7c6b62 100%);
  }
  .shapes { left: 0; top: 0; width: 897px; height: 1160px; }
  .logo-panel {
    left: 50px; top: 0; width: 231px; height: 332px;
    background: rgba(246,247,249,.93);
    display: flex; flex-direction: column; align-items: center; justify-content: center; gap: 12px;
  }
  .logo-mark { width: 90px; height: 90px; border: 3px solid #222; border-radius: 50%; }
  .logo-name {
    font-family: "Lato", sans-serif; font-weight: 700; font-size: 17px; color: #222;
    text-align: center; line-height: 1.25; width: 180px;
  }
  .council-title {
    left: 310px; top: 18px; font-family: "Oswald", sans-serif; font-weight: 500;
    font-size: 28px; color: var(--orange-soft); letter-spacing: .2px; white-space: nowrap;
  }
  .moment-photo { border-radius: 50%; border: 6px solid var(--ring); box-shadow: 0 0 0 4px #fff inset; }
  .moment-photo.music { left: 475px; top: 305px; width: 196px; height: 196px;
    background: radial-gradient(circle at 45% 55%, #c9a78e 0%, #8d6f64 40%, #d8d2cc 100%); }
  .moment-photo.drums { left: 636px; top: 379px; width: 216px; height: 216px;
    background: radial-gradient(circle at 50% 55%, #8a5a3c 0%, #b07a55 35%, #f3e6dc 100%); }
  .event-count {
    left: 51px; top: 383px; font-family: "Roboto Slab", serif; font-weight: 700;
    font-size: 54px; color: var(--orange-soft); white-space: nowrap;
  }
  .event-name {
    left: 51px; top: 447px; font-family: "Libre Baskerville", serif; font-style: italic; font-weight: 700;
    font-size: 30px; color: var(--navy); white-space: nowrap;
  }
  .divider { left: 0; top: 506px; width: 633px; height: 1px; background: #8fb7d8; }
  .tagline { left: 51px; top: 523px; font-family: "Lato", sans-serif; font-weight: 700; font-size: 24px; line-height: 32px; white-space: nowrap; }
  .tagline .accent { color: var(--orange); display: block; }
  .tagline .plain { color: var(--ink); display: block; }
  .theme-band { left: 0; top: 632px; width: 897px; height: 94px; background: rgba(205,211,216,.85); }
  .theme-line {
    left: 52px; top: 640px; font-family: "Libre Baskerville", serif; font-weight: 700;
    font-size: 31px; color: #4b4b4b; white-space: nowrap;
  }
  .theme-line .label { color: var(--sky); }
  .date-line {
    left: 52px; top: 687px; font-family: "Libre Baskerville", serif; font-weight: 700;
    font-size: 20px; color: #4b4b4b; white-space: nowrap;
  }
  .date-line .label { color: var(--sky); }
  .column { width: 380px; font-family: "PT Sans", sans-serif; font-size: 12.2px; line-height: 15.9px; color: var(--body-text); }
  .column.left { left: 52px; top: 748px; }
  .column.right { left: 465px; top: 748px; }
  .column h2 {
    font-family: "Libre Baskerville", serif; font-weight: 700; font-size: 16px;
    color: var(--navy); letter-spacing: .5px; margin-bottom: 8px;
  }
  .column p { text-align: justify; margin-bottom: 15px; }
  .column .note { font-weight: 700; color: #333; text-align: left; margin-bottom: 14px; }
  .column .note .due { color: var(--navy); }
  .column.right h2.gallery { margin-top: 2px; }
  .link-line { display: flex; align-items: center; gap: 8px; font-weight: 700; color: #333; margin-top: -2px; }
  .sponsor {
    top: 1047px; width: 181px; height: 53px; border: 1px solid #b9d3e6;
    background: rgba(255,255,255,.35);
    display: flex; align-items: center; justify-content: center; gap: 8px;
    font-family: "PT Sans", sans-serif; font-size: 13px; color: #5a7f5a;
  }
  .sponsor.host { left: 466px; }
  .sponsor.partner { left: 662px; color: #2e5f9e; }
  .sponsor .dot { width: 14px; height: 14px; border-radius: 50%; background: currentColor; }
  .venue {
    left: 54px; top: 1092px; font-family: "Lato", sans-serif; font-weight: 700;
    font-size: 16.5px; line-height: 21px; color: #fff; white-space: nowrap;
  }
  .contact {
    left: 470px; top: 1118px; height: 42px; display: flex; align-items: center; gap: 14px;
    font-family: "PT Sans", sans-serif; font-size: 13.5px; color: #fff; white-space: nowrap;
  }
  .contact span { display: flex; align-items: center; gap: 7px; }
  .social-square { width: 15px; height: 15px; background: #fff; border-radius: 2px; }
</style>
</head>
<body>
<main class="poster">
  <div class="hero-photo" role="img" aria-label="Group photo of teenagers from many faith communities gathered on a stage with a red curtain"></div>

  <svg class="shapes" viewBox="0 0 897 1160" aria-hidden="true">
    <path d="M0,300 C260,262 560,300 897,420 L897,1160 L0,1160 Z" fill="#e6f1f9"/>
    <path d="M0,385 C220,318 470,308 700,382 L897,450 L897,1160 L0,1160 Z" fill="#cde6f6"/>
    <path d="M0,372 C210,318 460,306 690,372 L897,440" fill="none" stroke="#f78f20" stroke-width="5"/>
    <path d="M0,382 C215,328 465,316 694,382 L897,450" fill="none" stroke="#2f86e0" stroke-width="6"/>
    <path d="M0,1083 L398,1083 Q432,1083 436,1118 L440,1160 L0,1160 Z" fill="#ffffff"/>
    <rect x="434" y="1118" width="463" height="42" fill="#58595b"/>
    <path d="M0,1089 L392,1089 Q424,1089 428,1122 L431,1160 L0,1160 Z" fill="#2f86e0"/>
  </svg>

  <div class="logo-panel">
    <div class="logo-mark"></div>
    <div class="logo-name">Harborview Teen Circle of PL</div>
  </div>

  <div class="council-title">Harborview Teen Circle of Pine Lakes's</div>

  <div class="moment-photo music" role="img" aria-label="Teen musicians performing with microphones and a stringed instrument"></div>
  <div class="moment-photo drums" role="img" aria-label="Teen playing taiko drums at the festival"></div>

  <div class="event-count">14th Annual</div>
  <div class="event-name">Kindred Gathering &amp; Fair</div>
  <div class="divider"></div>
  <div class="tagline">
    <span class="accent">TEENS EXPRESSING THEIR FAITH THROUGH</span>
    <span class="plain">ART, MUSIC, AND DIALOGUE</span>
  </div>

  <div class="theme-band"></div>
  <div class="theme-line"><span class="label">THIS YEAR'S THEME :</span> Who Are You ?</div>
  <div class="date-line"><span class="label">Date :</span> Sunday, March 11th, 2018, <span class="label">Time :</span> 11:00am-5:00pm</div>

  <section class="column left">
    <h2>KINDRED GATHERING</h2>
    <p>The purpose of this Interfaith Youth Forum is to bring together young people from diverse ethnic, cultural, and religious backgrounds, and to engage them in dialogue. True dialogue is a conversation on a common subject between two or more persons of differing points of view and/or backgrounds. We feel that this commitment to dialogue will affect relationships in a constructive way in our places of worship and in our community.</p>
    <p>The forum itself involves having eight religiously diverse high school-age students, one adult, and youth leader around each table to discuss common questions. Our youth leaders act as facilitators, but it is stressed that it is the students we want to hear from.</p>
    <p class="note" style="margin-top:22px;margin-bottom:12px">RSVP for our KINDRED GATHERING before <span class="due">February 18th, 2018</span><br>FORUM QUESTIONS Available online at</p>
    <div class="link-line">
      <svg width="18" height="18" viewBox="0 0 20 20" aria-hidden="true"><circle cx="10" cy="10" r="8" fill="none" stroke="#f78f20" stroke-width="2"/><ellipse cx="10" cy="10" rx="3.5" ry="8" fill="none" stroke="#f78f20" stroke-width="1.6"/><line x1="2" y1="10" x2="18" y2="10" stroke="#f78f20" stroke-width="1.6"/></svg>
      http://htcpl-example.org/home/kindred-fair/
    </div>
  </section>

  <section class="column right">
    <h2>FAITH FESTIVAL</h2>
    <p>The forum will include our Faith Festival portion of the program which families of the participants are welcomed to join. The Festival will include musical performances of all types from diverse religious communities. The differing performing arts include but are not limited to singing, dancing, instrumental music, storytelling, etc.</p>
    <p class="note">To Participate in our Faith Festival (Music, Song, Dance),<br>RSVP by <span class="due">February 11th, 2018</span></p>
    <h2 class="gallery">ART GALLERY</h2>
    <p style="margin-bottom:8px">This event will include and Art Gallery display of students' work, highlighting their expressions of faith, and artwork promoting learning, understanding, leadership, and service. Art includes any painting, illustration, sculpture, photography or other visual art.</p>
    <p class="note">Art Work for our Art Galley must be submitted by: March 3rd, 2018</p>
  </section>

  <div class="sponsor host"><span class="dot"></span>Congregation Ner Adamah</div>
  <div class="sponsor partner"><span class="dot"></span>Bright Path Allies</div>

  <div class="venue">Congregation Ner Adamah<br>4187 W Larkmont Rd. Santa Ana, CA 92705</div>

  <div class="contact">
    <span>
      <svg width="22" height="14" viewBox="0 0 22 14" aria-hidden="true"><rect x="6" y="1" width="15" height="12" fill="none" stroke="#fff" stroke-width="1.5"/><path d="M6,1 L13.5,8 L21,1" fill="none" stroke="#fff" stroke-width="1.5"/><line x1="0" y1="5" x2="4" y2="5" stroke="#fff" stroke-width="1.3"/><line x1="1" y1="9" x2="4" y2="9" stroke="#fff" stroke-width="1.3"/></svg>
      htcplorg@mailbox-example.com
    </span>
    <span>
      <svg width="16" height="16" viewBox="0 0 20 20" aria-hidden="true"><circle cx="10" cy="10" r="8" fill="none" stroke="#fff" stroke-width="2"/><ellipse cx="10" cy="10" rx="3.5" ry="8" fill="none" stroke="#fff" stroke-width="1.6"/><line x1="2" y1="10" x2="18" y2="10" stroke="#fff" stroke-width="1.6"/></svg>
      www.HTCPL-example.org
    </span>
    <span class="social-square" aria-label="Social page"></span>
  </div>
</main>
</body>
</html>
```